Downloadable PDF "Brochure?"

We have a Free download we will provide in exchange for an email address on our new Trailmark website. The website at www.venturetrailmark-example.com is in development and will look nothing like what it currently does, but you can go there and get a sense of what Trailmark is from the text on the website. (see the attached image 'site design' for the new redesigned website for aesthetics).

We are looking for a nice design for the document, that will represent the mostly text document well. We are not actually looking to print these at a printer so they don't have to be print ready. I went ahead and included the logo and colors and fonts file again just for reference.

Target Market(s)

Business Owners / Decision Makers

Requirements
Must have
• See attached document 'trailmark freebie' for text to be utilized in the finished deliverable.
• See the attached image 'Site Design' for the website aesthetic.

```html
<!DOCTYPE html>
<html lang="en">
<head>
<meta charset="utf-8">
<title>Trailmark – 10 Questions To Choose The Best Technology Advisor</title>
<link href="https://fonts.googleapis.com/css2?family=Cinzel:wght@400;600;700&family=Open+Sans:wght@400;600&display=swap" rel="stylesheet">
<style>
  :root{
    --slate:#2f3c45;
    --slate-dark:#1f2529;
    --orange:#c66f34;
    --text:#2b2b2b;
    --paper:#ffffff;
    --backdrop:#e9e6e1;
  }
  *{box-sizing:border-box;margin:0;padding:0}
  html,body{width:935px;height:1200px;overflow:hidden}
  body{background:var(--backdrop);position:relative;font-family:"Open Sans",Arial,sans-serif;color:var(--text)}
  .page{position:absolute;background:var(--paper);box-shadow:0 2px 8px rgba(0,0,0,.25);overflow:hidden;display:flex;flex-direction:column}
  .page-cover{left:51px;top:65px;width:404px;height:522px}
  .page-middle{left:51px;top:614px;width:404px;height:520px}
  .page-closing{left:484px;top:425px;width:429px;height:521px}

  .hero{position:relative;height:176px;background:linear-gradient(180deg,#c9a27c 0%,#e6d3bd 35%,#b9bcc2 70%,#eef0f2 100%)}
  .brand{position:absolute;left:28px;top:24px;display:flex;align-items:center;gap:10px}
  .brand-mark{width:34px;height:34px;border-radius:50%;background:var(--slate)}
  .brand-name{font-family:"Cinzel",serif;font-size:16px;font-weight:600;letter-spacing:1px;color:var(--slate)}
  .title-band{position:absolute;left:22px;right:22px;bottom:8px;height:20px;background:var(--slate);border-radius:10px;
    color:#fff;font-family:"Cinzel",serif;font-weight:700;font-size:11.5px;display:flex;align-items:center;justify-content:center;letter-spacing:.3px}

  .content{padding:6px 22px 0}
  .intro{font-size:6.1px;line-height:1.35;margin-bottom:6px}
  .question{font-family:"Cinzel",serif;font-weight:600;font-size:8.2px;line-height:1.15;text-align:center;color:var(--slate);margin:9px 8px 0}
  .question em{font-style:normal;color:var(--orange)}
  .divider{display:flex;justify-content:center;margin:3px 0 4px}
  .divider span{display:block;height:1.5px;width:11px;background:var(--slate)}
  .divider span+span{background:var(--orange)}
  .answer{font-size:6.1px;line-height:1.36;text-align:justify}

  .photo-strip{margin-top:auto;height:74px;background:linear-gradient(90deg,#3b3430,#8a8d93 45%,#d9d6d2 70%,#6d5848)}
  .photo-desk{margin-top:10px;height:213px;background:linear-gradient(135deg,#4a3426,#8a6446 40%,#c9c7c4 60%,#6e4d34)}
  .contact-bar{height:30px;background:var(--slate-dark);display:flex;align-items:center;padding:0 16px;gap:22px;color:#fff;font-size:5.3px}
  .contact-title{font-family:"Cinzel",serif;color:var(--orange);font-size:8.5px;font-weight:600}
  .contact-item{display:flex;align-items:center;gap:4px;line-height:1.2}
  .contact-item svg{flex:none}
</style>
</head>
<body>

<section class="page page-cover">
  <header class="hero" role="img" aria-label="City skyline at sunrise">
    <div class="brand"><span class="brand-mark"></span><span class="brand-name">Trailmark</span></div>
    <h1 class="title-band">10 Questions To Choose The Best Technology Advisor</h1>
  </header>
  <div class="content">
    <p class="intro">When you choose a technology advisor whether it be a Managed Service Provider, fractional CIO or a full-time CIO you need to make sure that they understand business just as much as they understand technology. Some of the biggest complaints about the IT department are that they just don't "Get it". The questions below should help you determine whether or not they have a technology mindset or a business mindset.</p>

    <h2 class="question">What is <em>scalability</em>? How important is it from a technology perspective on a scale of 1-&gt;10 with 10 being the highest? What all does scalability impact?</h2>
    <div class="divider"><span></span><span></span></div>
    <p class="answer">This question is designed to get a reading on the person's mindset. A typical technology-minded response would be something describing the ability of systems or software to scale by adding additional resources. When working from a business point of view, however, you want to see it defined as the ability for the organization to support increased volume without sacrificing margins. The importance of this concept cannot be overstated and should be a 9 or 10 in terms of ranking. Regarding impact, you want to see not just an understanding of having to spend money two or three times for a different solution to the same problem, but an acknowledgment of the 'total' cost, including adoption fatigue, the opportunity cost of change, and the competitive disadvantage it creates. For concepts of business scalability refer to 'Growing Wide' by Dale Everly.</p>

    <h2 class="question">Provide an <em>example</em> where you solved a problem <em>without</em> the use of <em>technology</em>.</h2>
    <div class="divider"><span></span><span></span></div>
    <p class="answer">Often technology-minded individuals become so wrapped up in the solutions themselves they fail to realize a policy or process change is far more effective and simple than making changes to existing or introducing new technology. Asking for a specific example here should demonstrate the ability to think from a business mindset. For specific examples reference 'The Ember Project' by Lane, Hart, and Moss.</p>

    <h2 class="question">How do you go about <em>prioritizing solutions</em> in order of importance for implementation / adoption?</h2>
    <div class="divider"><span></span><span></span></div>
    <p class="answer">Answers here should include reference to some form of discovery process or a thorough evaluation at the operations level. One of the key skill sets for someone approaching technology from a business point of view is mapping solutions and their respective importance to business outcomes and (often more importantly) eliminating bottlenecks while respecting that some implementations must necessarily come before others to be viable. For reference on the Theory of Constraints see 'The Target' by Elias Gorman.</p>
  </div>
</section>

<section class="page page-middle">
  <div class="content">
    <h2 class="question">What is <em>Information Technology Debt</em>?</h2>
    <div class="divider"><span></span><span></span></div>
    <p class="answer">Stated simply, 'IT Debt' is a measurement of the out-of-date, incomplete or yet-to-be-defined technology changes. Debt occurs for a number of reasons, including lack of qualified personnel to implement the needed solutions (or recognize the problem in the first place); historical spending haunting the organization "we spent money on something like this before and look what it got us"; Fire-fighting (addressing issues purely reactively in a downward spiral leaving no time for fixing the real underlying problem); or most commonly, the budget being already allocated to other company endeavors that seem immediately more pressing. By recognizing what IT Debt is, the individual demonstrates an acknowledgment of how impactful it can be when neglected and not brought to the forefront of business planning sessions.</p>

    <h2 class="question">Provide an example where you argued against <em>implementing a technology solution</em> and why.</h2>
    <div class="divider"><span></span><span></span></div>
    <p class="answer">Despite it being seemingly obvious, using 'outside of budget' is not a good answer. Business-minded technology advisors should be intimately aware of how well a proposed solution will integrate into the existing company ecosystem (software tools already present, workflow, and processes), if it drives the company toward reducing/eliminating a bottleneck (and thereby creates more leverage), and if it fits the company's culture. If any of these are a no, the solution should be carefully examined for what it really offers the organization. If yes, the budget should be evaluated as a cost-benefit analysis, not a flat number 'not to exceed'.</p>

    <h2 class="question">What is your ideal method for <em>maintaining technology alignment</em> for the company?</h2>
    <div class="divider"><span></span><span></span></div>
    <p class="answer">You want to see a specific process envisioned here. At the very least a recommendation to be involved in business planning meetings or retreats, and ideally a standing technology focused meeting with leadership present should be argued for. For technology to be truly in alignment, it must fit the needs of the organization, not the other way around. This needs to come from the top level, and it means a representative must be present in critical business strategy meetings to understand where the company is headed, what operational constraints they are encountering, and what their short-term goals are. For an outline of how this model has been the underlying key to success for several well-known companies reference 'Steady to Strong' by Jon Carver.</p>

    <h2 class="question">How do you plan on <em>measuring and monitoring</em> the adoption success of a solution or project?</h2>
    <div class="divider"><span></span><span></span></div>
    <p class="answer">Technically minded individuals often look at the point of 'it's up and running and it all works', as where their responsibilities end. Someone with a business mindset should demonstrate that evaluating how well the solution has been adopted into the day to day workflow, and to what degree the solution has increased leverage or operational transparency are the true critical indicators of success. There should be a specific process of follow-up after implementation to flag adoption or workflow issues due to problems such as inadequate training, unforeseen incompatibilities (whether they be process or technology related), or simply resistance to change. These findings can then be brought back to leadership to evaluate how best to improve successful adoption going forward.</p>
  </div>
  <div class="photo-strip" role="img" aria-label="Business team reviewing charts on laptops"></div>
</section>

<section class="page page-closing">
  <div class="content" style="padding-top:16px">
    <h2 class="question" style="margin-top:10px">Provide an example where you had to balance customer and employee technology experience with security and compliance.</h2>
    <div class="divider"><span></span><span></span></div>
    <p class="answer">A critical role fulfilled by a technology advisor is being able to balance maintaining compliance and sound security practices with as painless of a technology experience as possible. They should be able to weigh the critical importance of protecting the organization from the negative public relations and liability of a security flaw while respecting a solution must be usable to be useful. Look for an example that demonstrates an understanding of both sides and strikes a balance without going to an extreme in either direction.</p>

    <h2 class="question">What would you do first, if you were selected as our advisor? Can you give me details on what your discovery or on-boarding process includes?</h2>
    <div class="divider"><span></span><span></span></div>
    <p class="answer">You are looking to make sure that they don't stop at the technology. There should be a higher focus on understanding what the company processes are and how the people inside the organization get work done. If they focus only on network, security, and disaster recovery assessments then they do not have a business mindset.</p>

    <h2 class="question">Can you give me an example of a time you gave a suggestion for a solution and it was not taken? Describe the solution and why it was important to the organization. And why do you think they didn't implement it?</h2>
    <div class="divider"><span></span><span></span></div>
    <p class="answer">When they describe why they think the solution was important do they simply talk about risk reduction or uptime improvements without tying them back to an organizational goal or bottleneck. Being able to demonstrate actual business value is a critical skill for a technology advisor. For reference on technical excellence in service of business objectives rather than blindly servicing requirements see 'A Chair in The Room' by Mark Sheldon.</p>
  </div>
  <div class="photo-desk" role="img" aria-label="Person working on a laptop at a wooden desk with documents and a phone"></div>
  <footer class="contact-bar">
    <span class="contact-title">Contact Us</span>
    <span class="contact-item">
      <svg width="7" height="9" viewBox="0 0 10 13"><path d="M5 0a5 5 0 0 0-5 5c0 4 5 8 5 8s5-4 5-8a5 5 0 0 0-5-5zm0 7a2 2 0 1 1 0-4 2 2 0 0 1 0 4z" fill="#c66f34"/></svg>
      <span>1200 Ridge Valley Road, Suite 100<br>Cedar Falls, TX 75000</span>
    </span>
    <span class="contact-item">
      <svg width="8" height="8" viewBox="0 0 12 12"><path d="M2.5 0.5l2 2.5-1.2 1.5a7 7 0 0 0 4.2 4.2L9 7.5l2.5 2-1 2C5 11.5 0.5 7 0.5 1.5z" fill="#c66f34"/></svg>
      <span>(555) 014-0199</span>
    </span>
    <span class="contact-item">
      <svg width="9" height="7" viewBox="0 0 12 9"><rect x=".5" y=".5" width="11" height="8" fill="none" stroke="#c66f34"/><path d="M.5.5 6 5l5.5-4.5" fill="none" stroke="#c66f34"/></svg>
      <span>hello@venturetrailmark-example.com</span>
    </span>
  </footer>
</section>

</body>
</html>
```